New business needs a slick but classy, conservative and elegant Legal Letterhead

We need a new letterhead for a law firm that is slick but very classy and also understated.

The name of the firm is K.L. Marlow Lawyers.

All information about the Law firm should appear at the top of the page. Please no firm information in the footer.

It should have a clean, neat look. No watermarks or bold graphics please.

Info should include the name of the law firm, both the street address and postal address, the phone number and the fax number, the names of the principals, the website. We have attached a word document that contains the relevant information.

We have attached a copy of the business card for further information purposes.

We also need a law society logo to appear (probably on the bottom right hand side of the letterhead?) that states our affiliation to the law society. It is attached and must not be altered in any way. It can be small.

The only footer text we require is as worded in the attached information document.

We would like to see designs that use red and white - in an understated, elegant style - not too modern or too gaudy looking.

The final design should communicate that we mean business and that we are to be trusted.
Updates

Please insert firm's name K.L. Marlow Lawyers on letterhead! I have removed KLM logo as designers were using it instead of the name of the firm. Thank you!

Industry/Entity Type

Legal

Font styles to use
Serif

Colors
ec1f27
ffffff

Requirements
Must have
• All information contained in the word document attached - firm details, law society affiliation logo, firm name & firm logo, principals' names.
Should not have
• watermarks
• no firm details in footer

```html
<!DOCTYPE html>
<html lang="en">
<head>
<meta charset="utf-8">
<title>K.L. Marlow Lawyers — Letterhead</title>
<link href="https://fonts.googleapis.com/css2?family=Libre+Baskerville:wght@400;700&family=Open+Sans:wght@400;600;700&display=swap" rel="stylesheet">
<style>
  :root {
    --brand-red: #ec1f27;
    --ink: #2b2b2b;
    --muted: #6b6b6b;
    --paper: #ffffff;
    --footer-grey: #eeeeee;
    --rule-grey: #d9d9d9;
  }
  html, body {
    margin: 0;
    padding: 0;
    width: 891px;
    height: 1200px;
    overflow: hidden;
    background: var(--paper);
  }
  .letterhead {
    position: relative;
    width: 891px;
    height: 1200px;
    background: var(--paper);
    overflow: hidden;
  }
  .masthead {
    position: absolute;
    left: 45px;
    top: 30px;
    display: flex;
    align-items: center;
    gap: 18px;
  }
  .brand-mark {
    width: 62px;
    height: 38px;
    background: var(--brand-red);
    border-radius: 4px;
  }
  .firm-name {
    font-family: "Libre Baskerville", Georgia, serif;
    font-weight: 700;
    font-size: 27px;
    letter-spacing: 0.5px;
    color: var(--ink);
    text-transform: uppercase;
    margin: 0;
    padding-top: 10px;
  }
  .contact-list {
    position: absolute;
    left: 728px;
    top: 20px;
    margin: 0;
    padding: 0;
    list-style: none;
    font-family: "Open Sans", Arial, sans-serif;
    font-size: 8.5px;
    line-height: 12.5px;
    color: var(--muted);
  }
  .contact-list li {
    display: flex;
    gap: 6px;
  }
  .contact-list .label {
    color: var(--brand-red);
    font-weight: 700;
    width: 8px;
  }
  .header-rule {
    position: absolute;
    left: 0;
    top: 96px;
    width: 891px;
    height: 2px;
    background: var(--brand-red);
  }
  .footer-band {
    position: absolute;
    left: 0;
    bottom: 0;
    width: 891px;
    height: 48px;
    background: var(--footer-grey);
  }
  .footer-accent {
    position: absolute;
    left: 0;
    top: 1148px;
  }
  .footer-note {
    position: absolute;
    left: 45px;
    top: 1166px;
    margin: 0;
    font-family: "Open Sans", Arial, sans-serif;
    font-weight: 600;
    font-size: 12px;
    color: var(--ink);
  }
  .society-badge {
    position: absolute;
    left: 808px;
    top: 1148px;
    width: 40px;
    height: 40px;
    background: var(--brand-red);
    opacity: 0.85;
  }
</style>
</head>
<body>
  <main class="letterhead">
    <header class="masthead">
      <div class="brand-mark"></div>
      <h1 class="firm-name">K.L. Marlow Lawyers</h1>
    </header>

    <ul class="contact-list">
      <li><span class="label">A</span><span>Suite 2, 14 Harbour Lane</span></li>
      <li><span class="label"></span><span>PO Box 318, Northvale NSW 2000</span></li>
      <li><span class="label">T</span><span>02 5550 0142</span></li>
      <li><span class="label">F</span><span>02 5550 0143</span></li>
      <li><span class="label">W</span><span>www.klmarlow.com.au</span></li>
    </ul>

    <div class="header-rule"></div>

    <div class="footer-band"></div>
    <svg class="footer-accent" width="891" height="8" viewBox="0 0 891 8" aria-hidden="true">
      <rect x="0" y="2" width="891" height="2" fill="var(--brand-red)"/>
      <polygon points="0,0 330,0 360,8 0,8" fill="var(--brand-red)"/>
    </svg>
    <p class="footer-note">Liability limited by a scheme approved under Professional Standards</p>

    <div class="society-badge" role="img" aria-label="Law society affiliation badge"></div>
  </main>
</body>
</html>
```